Brookvale Renovations - Get the creative juices going!!

Brookvale does not do the actual renovation work. The company provides high end project management of renovation (primarily residential - with an eye toward commercial) The renovation work could look very different between projects. This company manages the work of contractors, architects and interior designers (either subcontracted directly by Brookvale or hired by the client and entrusted to Brookvale to manage). Clients are high end in the economic scale and the card needs to have a high end feel to it.

The owner is female, but the audience will be heavily slanted male. It should not be a "feminine" or "masculine" looking card. If anything, slant more on the masculine side. Clean, simple, yet creative and artistically appealing. The card design should complement and in no way compete with the logo.

When people think of our company: trust, integrity, dynamic, limitless possibilities, transition, energy, creative. We plan to expand in the future to be international.

There will also be a contest running for stationary. Please check that section, as well.

***Black is 80-90 percent black. Not stark black

Tight timeline. Needs cards printed quickly!

```html
<!DOCTYPE html>
<html lang="en">
<head>
<meta charset="utf-8">
<title>Brookvale Renovations – Business Card</title>
<link href="https://fonts.googleapis.com/css2?family=Open+Sans:wght@300;400;600;700&display=swap" rel="stylesheet">
<style>
  :root{
    --page:#e9e8e6;
    --card-dark:#2f3133;
    --card-mid:#4a4c4f;
    --ink:#1e1f21;
    --teal:#1bc5c0;
    --teal-deep:#12a9a5;
    --white:#f4f6f6;
    --muted:#cfd3d4;
  }
  *{box-sizing:border-box;margin:0;padding:0}
  html,body{width:1200px;height:1023px;overflow:hidden}
  body{
    background:var(--page);
    font-family:"Open Sans",Arial,sans-serif;
    display:flex;flex-direction:column;align-items:center;justify-content:center;gap:16px;
  }
  .card{
    position:relative;width:840px;height:480px;overflow:hidden;
    background:linear-gradient(135deg,var(--card-mid) 0%,var(--card-dark) 55%,var(--ink) 100%);
    box-shadow:0 10px 26px rgba(0,0,0,.25);
  }
  /* front */
  .brand{position:absolute;left:70px;top:72px;display:flex;align-items:center;gap:18px}
  .brand-square{width:46px;height:46px;background:var(--teal)}
  .brand-name{
    color:var(--white);font-weight:600;font-size:34px;letter-spacing:1.5px;text-transform:uppercase;
  }
  .person{position:absolute;left:70px;top:190px}
  .person-name{color:var(--teal);font-weight:400;font-size:30px;letter-spacing:1.5px;text-transform:uppercase}
  .person-title{color:var(--white);font-size:20px;margin-top:6px}
  .contacts{position:absolute;left:70px;top:296px;list-style:none}
  .contacts li{display:flex;align-items:center;gap:12px;color:var(--white);font-size:19px;margin-bottom:12px}
  .contact-icon{width:24px;height:24px;flex:none}
  .address{
    position:absolute;left:70px;bottom:46px;color:var(--teal);
    font-size:19px;letter-spacing:1px;text-transform:uppercase;
  }
  .accent-panel{
    position:absolute;right:0;top:0;width:180px;height:100%;
    background:linear-gradient(180deg,var(--teal) 0%,var(--teal-deep) 100%);
  }
  .accent-rule{position:absolute;right:180px;top:0;width:34px;height:100%;background:var(--ink)}
  /* back */
  .back-panel{
    position:absolute;left:0;top:0;width:100%;height:100%;
    background:linear-gradient(160deg,var(--teal) 0%,var(--teal-deep) 60%,var(--ink) 100%);
  }
  .back-band{position:absolute;left:0;top:0;width:46%;height:100%;background:var(--card-dark)}
  .back-brand{
    position:absolute;left:0;top:0;width:100%;height:100%;
    display:flex;align-items:center;justify-content:center;gap:18px;
  }
  .back-brand .brand-name{font-size:46px}
</style>
</head>
<body>
  <section class="card card-front" aria-label="Business card front">
    <div class="accent-rule"></div>
    <div class="accent-panel" role="img" aria-label="Teal brand accent area"></div>
    <div class="brand">
      <span class="brand-square"></span>
      <span class="brand-name">Brookvale Renovations</span>
    </div>
    <div class="person">
      <p class="person-name">Jordan Ellery</p>
      <p class="person-title">CEO</p>
    </div>
    <ul class="contacts">
      <li>
        <svg class="contact-icon" viewBox="0 0 24 24" aria-hidden="true">
          <circle cx="12" cy="12" r="12" fill="#1bc5c0"/>
          <path d="M8.2 6.5l2 2.2-1 1.4c.7 1.5 1.9 2.7 3.4 3.4l1.4-1 2.2 2-.9 1.8c-4.3-.4-7.7-3.8-8.1-8.1z" fill="#2f3133"/>
        </svg>
        <span>415-555-0187</span>
      </li>
      <li>
        <svg class="contact-icon" viewBox="0 0 24 24" aria-hidden="true">
          <circle cx="12" cy="12" r="12" fill="#1bc5c0"/>
          <rect x="6" y="8" width="12" height="8" rx="1" fill="#2f3133"/>
          <path d="M6.5 8.5l5.5 4 5.5-4" stroke="#1bc5c0" stroke-width="1.2" fill="none"/>
        </svg>
        <span>Jordan@BrookvaleRenovations.com</span>
      </li>
    </ul>
    <p class="address">240 Harlow St, Oakridge CA 94110</p>
  </section>

  <section class="card card-back" aria-label="Business card back">
    <div class="back-panel" role="img" aria-label="Teal and charcoal brand background"></div>
    <div class="back-band"></div>
    <div class="back-brand">
      <span class="brand-square"></span>
      <span class="brand-name">Brookvale</span>
    </div>
  </section>
</body>
</html>
```